Anzeigengestaltung für Immobilienmakler für Wohnimmobilien
Zielgruppe
Immobilienmakler für Wohnimmobilien
Aufgabenstellung
Die Maße der Zeitungsanzeige sind 60 mm in der Höhe und 125 in der Breite, Dateiformat ist jpg oder Pdf mit 300dpi.
Bitte eines der zur Verfügung gestellten Logos verwenden
Folgender Text soll in der Anzeige enthalten sein:
Ihr kompetenter Immobilienmakler im Ennepe-Ruhr-Kreis
Lindenweg 7 - 45549 Sprockhövel
Tel. 0202 - 47315526 - www.wohnfeld.de
Optionaler zusätzlicher Text, falls noch Platz in der Anzeige ist:
Gerne bieten wir Ihnen ein unverbindliches Beratungsgespräch, sowie eine
kostenlose Wertermittlung an

```html
<!DOCTYPE html>
<html lang="de">
<head>
<meta charset="utf-8">
<title>Wohnfeld – Anzeige</title>
<link href="https://fonts.googleapis.com/css2?family=Open+Sans:wght@400;700&display=swap" rel="stylesheet">
<style>
  :root {
    --page: #ffffff;
    --frame: #b9b9b9;
    --ink: #45474b;
    --muted: #ababab;
    --rule: #c4c4c4;
    --photo-light: #eeebe6;
    --photo-mid: #d9cfc4;
    --photo-warm: #b98a6c;
  }
  html, body {
    margin: 0;
    padding: 0;
    width: 1200px;
    height: 846px;
    overflow: hidden;
    background: var(--page);
    font-family: "Open Sans", Arial, sans-serif;
  }
  .ad {
    position: absolute;
    left: 242px;
    top: 250px;
    width: 706px;
    height: 339px;
    box-sizing: border-box;
    border: 2px solid var(--frame);
    box-shadow: 0 1px 3px rgba(0,0,0,0.18);
    background: var(--page);
    overflow: hidden;
  }
  .ad__photo {
    position: absolute;
    left: 0;
    top: 0;
    width: 308px;
    height: 100%;
    background:
      radial-gradient(ellipse at 25% 90%, var(--photo-warm) 0%, rgba(185,138,108,0.55) 30%, rgba(185,138,108,0) 60%),
      linear-gradient(100deg, var(--photo-mid) 0%, var(--photo-light) 45%, #f4f2ef 70%, #e4e1dc 100%);
  }
  .ad__brand {
    position: absolute;
    left: 335px;
    top: 30px;
    font-size: 19px;
    font-weight: 400;
    letter-spacing: 5px;
    color: var(--ink);
  }
  .ad__headline {
    position: absolute;
    left: 327px;
    top: 80px;
    margin: 0;
    font-size: 27px;
    line-height: 31px;
    color: var(--ink);
    font-weight: 400;
  }
  .ad__headline strong { font-weight: 700; }
  .ad__offer {
    position: absolute;
    left: 327px;
    top: 183px;
    margin: 0;
    font-size: 16px;
    line-height: 19px;
    color: var(--ink);
  }
  .ad__rule {
    position: absolute;
    left: 325px;
    top: 259px;
    width: 360px;
    height: 1px;
    background: var(--rule);
  }
  .ad__contact {
    position: absolute;
    left: 326px;
    top: 276px;
    margin: 0;
    font-size: 16px;
    line-height: 19px;
    color: var(--muted);
    font-style: normal;
  }
  .ad__contact strong { font-weight: 700; }
</style>
</head>
<body>
  <div class="ad">
    <div class="ad__photo" role="img" aria-label="Foto: Maklerin übergibt einem Paar in einer hellen Wohnung den Schlüssel"></div>
    <div class="ad__brand">WOHNFELD</div>
    <h1 class="ad__headline"><strong>Ihr kompetenter<br>Immobilienmakler</strong><br>im Ennepe-Ruhr-Kreis</h1>
    <p class="ad__offer">Gerne bieten wir Ihnen ein unverbindliches<br>Beratungsgespräch, sowie eine kostenlose<br>Wertermittlung an.</p>
    <div class="ad__rule"></div>
    <address class="ad__contact">Lindenweg 7 - 45549 Sprockhövel<br>Tel. 0202 - 47315526 · <strong>www.wohnfeld.de</strong></address>
  </div>
</body>
</html>
```